Corvane Electronics, Inc. Business card

Incorporate a globe.
We repair electronics, sell electronic parts, and we recycle electronics. We've been in business since 1982. A technology feel to the card is preferred. I want to be able to give this card to a client from different industries and make it relate-able. I don't have a logo that I've been partial to in the past. It is not necessary in this case.

Target Market(s)

Consumer, Industrial, Business, Medical

Industry/Entity Type

Business

Contact Information for Business Card

4518 Maple Crest Blvd. Dallas, TX 75207
214-555-0187 main 214-555-0143 fax
Paul Bredesen VP

Font styles to use
Serif

Requirements
Must have
• Technology feel
Nice to have
• Metallic look
Should not have
• no pastel colors

```html
<!DOCTYPE html>
<html lang="en">
<head>
<meta charset="utf-8">
<title>Corvane Electronics, Inc. — Business Card</title>
<link rel="stylesheet" href="https://fonts.googleapis.com/css2?family=Tinos&family=Noto+Serif&display=swap">
<style>
  :root {
    --page: #ffffff;
    --ink-dark: #1f1f21;
    --ink-light: #f4f4f4;
    --steel-light: #e6e7e9;
    --steel-mid: #b8babd;
    --steel-dark: #8e9094;
    --accent-blue: #1a6fc4;
    --card-black: #1c1c1e;
    --card-charcoal: #3a3a3c;
  }
  * { box-sizing: border-box; margin: 0; padding: 0; }
  html, body {
    width: 1200px; height: 993px; overflow: hidden;
    background: var(--page);
  }
  .canvas { position: relative; width: 1200px; height: 993px; }

  .card {
    position: absolute; left: 252px; width: 658px; height: 402px; overflow: hidden;
  }
  .card-front { top: 75px;
    background: linear-gradient(90deg, var(--card-black) 0%, var(--card-charcoal) 35%, #262628 50%, var(--card-charcoal) 65%, var(--card-black) 100%);
  }
  .card-back { top: 525px;
    background:
      repeating-linear-gradient(90deg, rgba(255,255,255,.18) 0 1px, rgba(0,0,0,.06) 1px 2px, rgba(255,255,255,0) 2px 4px, rgba(0,0,0,.08) 4px 5px, rgba(255,255,255,0) 5px 7px),
      linear-gradient(180deg, var(--steel-mid) 0%, var(--steel-light) 55%, var(--steel-mid) 100%);
  }
  .card-art { position: absolute; inset: 0; width: 100%; height: 100%; }

  .heading {
    position: absolute; left: 0; width: 100%; top: 42px; text-align: center;
    font-family: "Noto Serif", Georgia, serif; font-size: 38px; font-weight: 400; line-height: 1;
    color: var(--accent-blue); padding-left: 6px;
  }
  .contact-line {
    position: absolute; left: 136px;
    font-family: "Tinos", "Times New Roman", serif; font-size: 26px; font-weight: 400; line-height: 1;
    color: var(--ink-light); white-space: nowrap;
  }
  .contact-address { top: 175px; }
  .contact-phone { top: 221px; }
  .contact-name { top: 267px; }

  .back-text {
    position: absolute; left: 0; width: 100%; text-align: center;
    font-family: "Tinos", "Times New Roman", serif; font-weight: 400; color: var(--ink-dark);
  }
  .since { top: 62px; font-size: 27px; }
  .company-name { top: 200px; font-size: 24px; }
  .tagline { top: 272px; font-size: 25px; line-height: 33px; }
</style>
</head>
<body>
<main class="canvas">

  <section class="card card-front" aria-label="Card front">
    <svg class="card-art" viewBox="0 0 658 402" aria-hidden="true">
      <defs>
        <linearGradient id="band-steel" x1="0" x2="1" y1="0" y2="0">
          <stop offset="0" stop-color="#9ea0a4"/>
          <stop offset=".2" stop-color="#d8d9db"/>
          <stop offset=".4" stop-color="#a9abae"/>
          <stop offset=".6" stop-color="#e4e5e7"/>
          <stop offset=".8" stop-color="#b3b5b8"/>
          <stop offset="1" stop-color="#a0a2a6"/>
        </linearGradient>
        <linearGradient id="strip-steel" x1="0" x2="0" y1="0" y2="1">
          <stop offset="0" stop-color="#f0f0f0"/>
          <stop offset=".5" stop-color="#b4b6b9"/>
          <stop offset="1" stop-color="#d6d7d9"/>
        </linearGradient>
      </defs>
      <path class="top-band" d="M0 0H658V77H458L424 113H246L210 77H0Z" fill="url(#band-steel)"/>
      <path class="band-edge" d="M0 77H210L246 113H424L458 77H658" fill="none" stroke="#6e7074" stroke-width="2"/>
      <path class="accent-line" d="M0 59H208L244 94H424L458 59H658" fill="none" stroke="var(--accent-blue)" stroke-width="3"/>
      <rect class="rivet-strip" x="0" y="349" width="658" height="25" fill="url(#strip-steel)"/>
      <g class="rivets" fill="#6a6c70" stroke="#3e4044" stroke-width="1">
        <circle cx="73" cy="361" r="5"/><circle cx="124" cy="361" r="5"/><circle cx="175" cy="361" r="5"/>
        <circle cx="227" cy="361" r="5"/><circle cx="278" cy="361" r="5"/><circle cx="329" cy="361" r="5"/>
        <circle cx="380" cy="361" r="5"/><circle cx="431" cy="361" r="5"/><circle cx="483" cy="361" r="5"/>
        <circle cx="534" cy="361" r="5"/><circle cx="585" cy="361" r="5"/>
      </g>
      <path class="icon-pin" d="M99 173c-6.6 0-11 4.8-11 10.6 0 7.6 11 19.4 11 19.4s11-11.8 11-19.4c0-5.8-4.4-10.6-11-10.6zm0 15a4.4 4.4 0 1 1 0-8.8 4.4 4.4 0 0 1 0 8.8z" fill="var(--accent-blue)"/>
      <path class="icon-phone" d="M92 217c2-1.5 4-1 5 .8l2.5 4.5c.8 1.5.3 3-1 4l-1.6 1.2c1.5 3.5 4.5 6.5 8 8l1.2-1.6c1-1.3 2.5-1.8 4-1l4.5 2.5c1.8 1 2.3 3 .8 5l-2 2.4c-1.5 1.6-4 2-6.5 1-8-3.4-14-9.4-17.3-17.4-1-2.5-.6-5 1-6.5z" fill="var(--accent-blue)"/>
    </svg>
    <h1 class="heading">Contact</h1>
    <p class="contact-line contact-address">4518 Maple Crest Blvd. Dallas, TX 75207</p>
    <p class="contact-line contact-phone">214-555-0187 main 214-555-0143 fax</p>
    <p class="contact-line contact-name">Paul Bredesen VP</p>
  </section>

  <section class="card card-back" aria-label="Card back">
    <svg class="card-art" viewBox="0 0 658 402" aria-hidden="true">
      <defs>
        <radialGradient id="screw-head" cx=".4" cy=".35" r=".7">
          <stop offset="0" stop-color="#f2f2f2"/>
          <stop offset=".7" stop-color="#a5a7aa"/>
          <stop offset="1" stop-color="#5e6064"/>
        </radialGradient>
        <radialGradient id="name-mark" cx=".38" cy=".32" r=".75">
          <stop offset="0" stop-color="#f4f4f5"/>
          <stop offset=".6" stop-color="#9a9ca0"/>
          <stop offset="1" stop-color="#4e5054"/>
        </radialGradient>
      </defs>
      <g class="screws" stroke="#4a4c50" stroke-width="1.5">
        <g><circle cx="39" cy="51" r="13" fill="url(#screw-head)"/><path d="M31 59L47 43" stroke-width="3"/></g>
        <g><circle cx="618" cy="51" r="13" fill="url(#screw-head)"/><path d="M606 51H630" stroke-width="3"/></g>
        <g><circle cx="39" cy="353" r="13" fill="url(#screw-head)"/><path d="M27 353H51" stroke-width="3"/></g>
        <g><circle cx="618" cy="353" r="13" fill="url(#screw-head)"/><path d="M618 341V365" stroke-width="3"/></g>
      </g>
      <circle class="name-mark" cx="329" cy="150" r="34" fill="url(#name-mark)"/>
    </svg>
    <p class="back-text since">Since 1982</p>
    <p class="back-text company-name">Corvane Electronics, Inc.</p>
    <p class="back-text tagline">We repair electronics, sell electronic parts,<br>and recycle electronics</p>
  </section>

</main>
</body>
</html>
```